Meditation for IVF and infertility

I need a flyer inviting IVF patients to join my Meditation class, I would like to offer free meditation to ivf women and for couples this class is free every Thursday night at 5 pm
2437 west harlow ave suite K Santa Barbara Ca 93142
quillbrook-stillness.com for more details

```html
<!DOCTYPE html>
<html lang="en">
<head>
<meta charset="utf-8">
<title>Meditation for Infertility &amp; IVF — Quillbrook Stillness</title>
<link rel="stylesheet" href="https://fonts.googleapis.com/css2?family=Zilla+Slab:wght@300;400;600;700&display=swap">
<style>
  :root {
    --backdrop: #dcdcdc;
    --paper: #ffffff;
    --photo-light: #eeeef3;
    --photo-mid: #e1e1e8;
    --photo-warm: #d8cfca;
    --ink: #55565a;
    --ink-dark: #2f3033;
    --taupe: #d6cbc6;
    --peach: #eddcd0;
    --charcoal: #58595b;
    --accent: #e9cdb9;
    --accent-text: #d9b59c;
  }
  * { box-sizing: border-box; margin: 0; padding: 0; }
  html, body {
    width: 1200px; height: 892px; overflow: hidden;
    background: var(--backdrop);
    font-family: "Zilla Slab", Georgia, serif;
  }
  .flyer {
    position: absolute; left: 75px; top: 71px;
    width: 1050px; height: 750px;
    background: var(--paper);
    overflow: hidden;
    box-shadow: 0 6px 18px rgba(0,0,0,.12);
  }
  .flyer__photo {
    position: absolute; inset: 0;
    background:
      radial-gradient(ellipse at 35% 30%, var(--photo-light) 0%, var(--photo-mid) 60%, transparent 100%),
      linear-gradient(200deg, var(--photo-light) 0%, var(--photo-mid) 55%, var(--photo-warm) 100%);
  }
  .headline {
    position: absolute; left: 48px; top: 36px;
    color: var(--ink);
  }
  .headline__word {
    display: block;
    font-weight: 400;
    font-size: 132px; line-height: .92;
    letter-spacing: 10px;
  }
  .headline__host {
    display: inline-block;
    margin-top: 22px;
    font-weight: 700; font-size: 25px; letter-spacing: 3px;
    color: var(--ink-dark); text-transform: uppercase;
  }
  .highlight {
    background: var(--accent);
    padding: 0 6px;
  }
  .headline__topic {
    display: block;
    margin-top: 10px;
    font-weight: 300; font-size: 66px; line-height: 1.05;
    color: var(--ink);
  }
  .panel {
    position: absolute; right: 0;
  }
  .panel--invite {
    top: 0; left: 563px; height: 250px;
    background: var(--taupe);
    padding: 38px 40px 0 42px;
    color: var(--ink);
    font-size: 23px; line-height: 1.32; letter-spacing: 1.2px;
    text-transform: uppercase;
  }
  .panel--invite strong { font-weight: 700; }
  .panel--invite .highlight { background: var(--paper); color: var(--accent-text); padding: 0 4px; }
  .panel--schedule {
    top: 253px; left: 563px; height: 237px;
    background: var(--peach);
    color: var(--ink);
    text-align: center;
    padding-top: 42px;
  }
  .schedule__day {
    display: block;
    font-weight: 300; font-size: 78px; letter-spacing: 5px; line-height: 1;
  }
  .schedule__time {
    display: block; margin-top: 10px;
    font-weight: 600; font-size: 38px; color: var(--ink-dark);
  }
  .panel--contact {
    top: 493px; left: 430px; height: 257px;
    background: var(--charcoal);
    border-radius: 130px 0 0 130px;
    color: #ececec;
    display: flex; flex-direction: column; justify-content: center;
    padding-left: 120px;
  }
  .brand {
    display: flex; align-items: center; gap: 14px;
    margin-bottom: 22px;
  }
  .brand__dot {
    width: 40px; height: 40px; border-radius: 50%;
    border: 2px solid #ffffff;
  }
  .brand__name {
    font-weight: 400; font-size: 30px; color: #ffffff;
  }
  .contact__line {
    font-size: 18px; line-height: 1.55; letter-spacing: .3px;
  }
  .contact__sep { font-size: 18px; line-height: 1; margin: 2px 0 4px 140px; }
  .contact__phone { color: var(--accent-text); }
  .contact__web { color: var(--accent-text); font-weight: 700; }
</style>
</head>
<body>
  <main class="flyer">
    <div class="flyer__photo" role="img" aria-label="Soft photo of a woman seated in a calm meditation pose in a bright, airy studio"></div>

    <h1 class="headline">
      <span class="headline__word">MEDI</span>
      <span class="headline__word">TATION</span>
      <span class="headline__host">with <span class="highlight">Mara Ellison</span></span>
      <span class="headline__topic">for Infertility<br>&amp; IVF.</span>
    </h1>

    <section class="panel panel--invite">
      <p><strong>Join</strong> instructor <span class="highlight">Mara Ellison</span> for a guided meditation session, for all IVF women &amp; couples regardless of where you are in your fertility journey.</p>
    </section>

    <section class="panel panel--schedule">
      <span class="schedule__day">THURSDAY</span>
      <span class="schedule__time">5:00 PM</span>
    </section>

    <section class="panel panel--contact">
      <div class="brand">
        <span class="brand__dot"></span>
        <span class="brand__name">Quillbrook Stillness</span>
      </div>
      <p class="contact__line">2437 west harlow ave suite K Santa Barbara Ca 93142</p>
      <p class="contact__sep">•</p>
      <p class="contact__line contact__phone">phone: (805) 555-0147</p>
      <p class="contact__line contact__web">quillbrook-stillness.com</p>
    </section>
  </main>
</body>
</html>
```